Stylist/Barber Standup Sign for Hair Regrowth Company

We want to design an attractive and eye-catching sign for hair stylists and barbers to sit on their workstations to attract the attention of their clients regarding hair loss and encourage them to speak to their stylist about it of they are would like to seek treatment.
50% of men and 25% of women suffer from hair loss but most are in denial that it is happening or too embarrassed to talk about it.

Copy for the flyer is as follows:

[Section 1:]
This flyer has been placed here/designed to spark conversation about hair loss

[Section 2:]
The truth is...
73% of people believe their hair is thinning
They are right

[Section 3:]
If you've got questions, your stylist or barber has answers.

Additional Background Information:

Primary target audience is men between the ages of 25-45, secondary target audience is men 46-60

Current Consumer Perception? (in the first person) “I’ve been thinking about my hair. I think it’s getting thinner and I’m scared, worried and don’t know what to do. But I don’t know if there is anything that really works. I’ve tried other things and nothing‘s worked.”

Tonality of materials? Very guy friendly, matter of fact, authoritative, its what you might hear from your best friend. Confident. Encouraging, but with a sense of urgency.

Please use our brand colors, but do not include our logo or brand name.
Colors are as follows:
Green: #4ca26f
Light Grey: #999999
Dark Grey: #262626

I have attached print templates in both PDF and Jpeg, please use those to provide final ready to print documents if you are selected.

Target Market(s)

Industry/Entity Type

Health And Wellness

Font styles to use
Sans Serif

Colors
00a990
ffffff
333333
cbcbcb

Requirements
Must have
• We want to get across the following messaging. Ideally you will submit a design using our copy and if you think you can do better, please feel free to submit another design with your own copy/messaging. If you can do it better we would love to select you :-)
• Our copy?
• This flyer has been placed here/designed to spark conversation about hair loss
• The truth is...
• 73% of people believe their hair is thinning
• They are right
• If you've got questions, your stylist or barber has answers
• Also please use our brand colors:
• Green: #4ca26f
• Light Grey: #999999
• Dark Grey: #262626
Should not have
• dont add any logos, images or ornate design. this needs to be simple, easy to ready and eye catching.
• do not use the color red in any capacity.

```html
<!DOCTYPE html>
<html lang="en">
<head>
<meta charset="utf-8">
<title>Hair Loss Conversation Sign</title>
<link rel="stylesheet" href="https://fonts.googleapis.com/css2?family=Source+Sans+3:wght@700&display=swap">
<style>
  :root {
    --surround: #000000;
    --sheet: #ffffff;
    --brand-green: #18ad92;
    --charcoal: #333333;
    --silver: #cbcbcb;
    --ink-light: #ffffff;
  }
  * { margin: 0; padding: 0; box-sizing: border-box; }
  html, body {
    width: 1200px;
    height: 1200px;
    overflow: hidden;
    background: var(--surround);
  }
  .canvas {
    position: relative;
    width: 1200px;
    height: 1200px;
    background: var(--surround);
    font-family: "Source Sans 3", "Myriad Pro", Arial, sans-serif;
    font-weight: 700;
    text-transform: uppercase;
  }
  .sheet {
    position: absolute;
    left: 167px;
    top: 25px;
    width: 879px;
    height: 1138px;
    background: var(--sheet);
    border: 1px solid #777;
  }
  .bubbles {
    position: absolute;
    inset: 0;
  }
  .bubble-green { fill: var(--brand-green); }
  .bubble-dark { fill: var(--charcoal); }
  .bubble-light { fill: var(--silver); }

  .message {
    position: absolute;
    letter-spacing: 0.2px;
  }
  .message--intro {
    left: 196px;
    width: 602px;
    top: 112px;
    font-size: 38px;
    line-height: 60.5px;
    text-align: center;
    color: var(--ink-light);
    word-spacing: 7px;
  }
  .message--truth {
    left: 458px;
    top: 404px;
    font-size: 40px;
    line-height: 60.5px;
    color: var(--ink-light);
    letter-spacing: -0.2px;
  }
  .message--truth .highlight { color: var(--brand-green); }
  .message--answers {
    left: 230px;
    width: 585px;
    top: 836px;
    font-size: 41px;
    line-height: 61px;
    text-align: center;
    color: var(--charcoal);
    letter-spacing: -0.2px;
  }
</style>
</head>
<body>
  <main class="canvas">
    <div class="sheet"></div>

    <svg class="bubbles" width="1200" height="1200" viewBox="0 0 1200 1200" aria-hidden="true">
      <g class="bubble-green">
        <rect x="196" y="58" width="602" height="366" rx="32"/>
        <path d="M270 420 C272 470 330 490 403 495 C365 480 345 455 345 420 Z"/>
      </g>
      <g class="bubble-dark">
        <rect x="420" y="372" width="603" height="365" rx="32"/>
        <path d="M962 733 C955 780 900 800 829 803 C870 785 890 760 892 733 Z"/>
      </g>
      <g class="bubble-light">
        <rect x="230" y="772" width="585" height="313" rx="32"/>
        <path d="M484 1081 C495 1115 540 1135 599 1138 C570 1125 553 1105 553 1081 Z"/>
      </g>
    </svg>

    <p class="message message--intro">
      This flyer has been<br>
      placed here / designed<br>
      to spark conversation<br>
      about hair loss
    </p>

    <p class="message message--truth">
      The truth is...<br>
      <span class="highlight">73%</span> of people believe<br>
      that their hair is<br>
      thinning<br>
      <span class="highlight">They are right</span>
    </p>

    <p class="message message--answers">
      If you've got questions,<br>
      your stylist or<br>
      barber has answers
    </p>
  </main>
</body>
</html>
```